New Webpage for High Class Expert Witness Services Company

We are looking for a minimalist design for a webpage that just has our logo and an entry form offer to connect with one of our Liaisons.
The entry form should just ask for Name, Email, Contact Info and Description of Project.

Company Name is: The Marlow Crest Advisory Services

Number of Pages Required

1 page

```html
<!DOCTYPE html>
<html lang="en">
<head>
<meta charset="UTF-8">
<title>Connect With Us – The Marlow Crest Advisory Services</title>
<link href="https://fonts.googleapis.com/css2?family=Cinzel:wght@400;500&family=Inter:wght@400&family=Montserrat:wght@500&display=swap" rel="stylesheet">
<style>
  :root {
    --page-bg: #131313;
    --pattern-tone: #171717;
    --text-light: #e6e6e6;
    --text-muted: #b8b8b8;
    --field-border: #5a5a5a;
    --divider: #6e6e6e;
    --gold: #d2b573;
    --gold-text: #c9a85c;
    --button-text: #fdf8ec;
  }
  * { box-sizing: border-box; margin: 0; padding: 0; }
  html, body {
    width: 1200px;
    height: 1200px;
    overflow: hidden;
    background: var(--page-bg);
  }
  .page {
    position: relative;
    width: 1200px;
    height: 1200px;
    display: flex;
    flex-direction: column;
    align-items: center;
    justify-content: center;
    padding: 0 120px;
  }
  .contour-backdrop {
    position: absolute;
    inset: 0;
    background: radial-gradient(ellipse at 50% 45%, var(--pattern-tone) 0%, var(--page-bg) 75%);
  }
  .brand, .divider, .contact-heading, .contact-intro, .contact-form {
    position: relative;
  }
  .brand {
    display: flex;
    align-items: center;
    gap: 16px;
  }
  .brand-mark {
    width: 18px;
    height: 18px;
    background: var(--text-light);
  }
  .brand-name {
    font-family: "Cinzel", serif;
    font-weight: 500;
    font-size: 34px;
    letter-spacing: 0.04em;
    color: var(--text-light);
  }
  .divider {
    width: 360px;
    height: 1px;
    background: var(--divider);
    margin: 34px 0 40px;
  }
  .contact-heading {
    font-family: "Cinzel", serif;
    font-weight: 400;
    font-size: 30px;
    letter-spacing: 0.06em;
    color: var(--gold-text);
    margin-bottom: 26px;
  }
  .contact-intro {
    font-family: "Inter", sans-serif;
    font-size: 17px;
    line-height: 1.6;
    text-align: center;
    color: var(--text-light);
    margin-bottom: 38px;
  }
  .contact-form {
    width: 960px;
    display: grid;
    grid-template-columns: 1fr 1fr;
    gap: 10px;
  }
  .field {
    height: 48px;
    border: 1px solid var(--field-border);
    border-radius: 8px;
    background: transparent;
    padding: 0 16px;
    font-family: "Inter", sans-serif;
    font-size: 13px;
    color: var(--text-light);
  }
  .field::placeholder { color: var(--text-muted); }
  .field-message {
    grid-column: 1 / -1;
    height: 86px;
    padding-top: 14px;
    resize: none;
  }
  .submit-button {
    grid-column: 1 / -1;
    height: 66px;
    border: none;
    border-radius: 4px;
    background: var(--gold);
    font-family: "Montserrat", sans-serif;
    font-weight: 500;
    font-size: 17px;
    letter-spacing: 0.05em;
    color: var(--button-text);
    cursor: pointer;
  }
</style>
</head>
<body>
  <main class="page">
    <div class="contour-backdrop" role="img" aria-label="Faint dark topographic contour pattern covering the page background"></div>

    <header class="brand">
      <span class="brand-mark"></span>
      <span class="brand-name">The Marlow Crest Advisory Services</span>
    </header>

    <div class="divider"></div>

    <h1 class="contact-heading">CONNECT WITH US</h1>

    <p class="contact-intro">
      Have a question or need assistance? Our liaison team is here to help.<br>
      Share your details below and we’ll get in touch with you shortly.
    </p>

    <form class="contact-form">
      <input class="field" type="text" placeholder="First Name">
      <input class="field" type="text" placeholder="Last Name">
      <input class="field" type="email" placeholder="Email Address">
      <input class="field" type="tel" placeholder="Phone Number">
      <textarea class="field field-message" placeholder="Details of your project*"></textarea>
      <button class="submit-button" type="submit">Submit</button>
    </form>
  </main>
</body>
</html>
```